New Business Card Design Project VORASTI-Italy

we are VORASTI-Italy
our company in the market for 3 years we are luxury cosmetic company and its about time for a facelift :)
i will like to have elegant luxurious and unique business card
that will give the person that get it a unique, luxurious and elegant impression
I'm VERY OPEN FOR NEW IDEAS , even duo i add a few files of things that i see on line and i like them

i add my logo as well
my website is VORASTI.COM
(if you would like to see the main style that we have)

Target Market(s)

adult that have money :)

Industry/Entity Type

Business

Contact Information for Business Card

Name - Paul Vorasti
Position - CEO and CO Founder
address - 4817 E Larkdale
telephone - 555-384-1962
email - paul@vorasti.com
fax - 555-384-1962
website - VORASTI.COM

Colors
000000
959595
fbee3e
ffffff

Requirements
Must have
• big logo in GOLD color
• elegant look
• impressive
Nice to have
• not must but maybe classy pattern background
• not must but maybe emblem
• maybe clear plastic business card
Should not have
• colors
• images

```html
<!DOCTYPE html>
<html lang="en">
<head>
<meta charset="utf-8">
<title>VORASTI Italy – Business Card</title>
<link href="https://fonts.googleapis.com/css2?family=Marcellus&family=Open+Sans:wght@400;600&display=swap" rel="stylesheet">
<style>
  :root {
    --stage: #2b2724;
    --card-dark: #0c0b0a;
    --card-mid: #1c1a18;
    --ornament: #3a3733;
    --gold: #e2b43a;
    --gold-deep: #c9982a;
    --tab-grey: #4a4846;
    --tab-grey-dark: #2f2e2c;
    --icon-dark: #1a1712;
  }
  * { margin: 0; padding: 0; box-sizing: border-box; }
  html, body { width: 1200px; height: 1200px; overflow: hidden; background: var(--stage); }
  .stage { width: 1200px; height: 1200px; display: flex; align-items: center; justify-content: center; }
  .card {
    position: relative; width: 1050px; height: 600px; border-radius: 22px; overflow: hidden;
    background: radial-gradient(ellipse at 30% 40%, var(--card-mid) 0%, var(--card-dark) 75%);
    box-shadow: 0 20px 50px rgba(0,0,0,.5);
  }
  .ornament-area {
    position: absolute; left: -260px; top: -40px; width: 680px; height: 680px; border-radius: 50%;
    background: radial-gradient(circle, transparent 50%, var(--ornament) 51%, rgba(58,55,51,.55) 70%, transparent 71%);
    opacity: .7;
  }
  .brand {
    position: absolute; left: 60px; top: 70px; width: 480px; text-align: center;
    font-family: "Marcellus", serif; color: var(--gold);
  }
  .brand-circle {
    width: 150px; height: 150px; margin: 0 auto 40px; border-radius: 50%;
    border: 6px solid var(--gold);
  }
  .brand-name { font-size: 96px; line-height: 1; letter-spacing: 1px; }
  .brand-origin { font-size: 34px; margin-top: 22px; letter-spacing: 2px; }
  .contacts {
    position: absolute; left: 600px; top: 58px; list-style: none;
    font-family: "Open Sans", sans-serif; color: var(--gold);
  }
  .contact-row { display: flex; align-items: center; height: 58px; margin-bottom: 22px; }
  .tab {
    width: 58px; height: 44px; margin-top: 14px;
    background: linear-gradient(180deg, var(--tab-grey) 0%, var(--tab-grey-dark) 100%);
  }
  .icon-box {
    width: 50px; height: 50px; background: var(--gold);
    display: flex; align-items: center; justify-content: center; margin-right: 20px;
  }
  .icon-box svg { width: 30px; height: 30px; }
  .contact-text { font-size: 24px; }
  .person-name { font-size: 30px; font-weight: 600; line-height: 1.1; }
  .person-role { font-size: 20px; }
</style>
</head>
<body>
<main class="stage">
  <section class="card">
    <div class="ornament-area" role="img" aria-label="Large faint decorative circular lattice ornament"></div>

    <div class="brand">
      <div class="brand-circle"></div>
      <div class="brand-name">VORASTI</div>
      <div class="brand-origin">ITALY</div>
    </div>

    <ul class="contacts">
      <li class="contact-row">
        <span class="tab"></span>
        <span class="icon-box"><svg viewBox="0 0 24 24" fill="var(--icon-dark)"><circle cx="12" cy="8" r="4.5"/><path d="M3 22c0-5 4-8 9-8s9 3 9 8z"/></svg></span>
        <div><div class="person-name">Paul Vorasti</div><div class="person-role">CEO and CO Founder</div></div>
      </li>
      <li class="contact-row">
        <span class="tab"></span>
        <span class="icon-box"><svg viewBox="0 0 24 24" fill="var(--icon-dark)"><path d="M12 2a7 7 0 0 0-7 7c0 5 7 13 7 13s7-8 7-13a7 7 0 0 0-7-7zm0 10a3 3 0 1 1 0-6 3 3 0 0 1 0 6z"/></svg></span>
        <span class="contact-text">4817 E Larkdale</span>
      </li>
      <li class="contact-row">
        <span class="tab"></span>
        <span class="icon-box"><svg viewBox="0 0 24 24" fill="var(--icon-dark)"><path d="M6.6 10.8a15 15 0 0 0 6.6 6.6l2.2-2.2c.3-.3.7-.4 1-.2 1.1.4 2.3.6 3.6.6.6 0 1 .4 1 1V20c0 .6-.4 1-1 1A17 17 0 0 1 3 4c0-.6.4-1 1-1h3.5c.6 0 1 .4 1 1 0 1.3.2 2.5.6 3.6.1.3 0 .7-.2 1z"/></svg></span>
        <span class="contact-text">555-384-1962</span>
      </li>
      <li class="contact-row">
        <span class="tab"></span>
        <span class="icon-box"><svg viewBox="0 0 24 24" fill="var(--icon-dark)"><path d="M2 5h20v14H2z"/><path d="M2 5l10 8 10-8" fill="none" stroke="var(--gold)" stroke-width="1.6"/></svg></span>
        <span class="contact-text">paul@vorasti.com</span>
      </li>
      <li class="contact-row">
        <span class="tab"></span>
        <span class="icon-box"><svg viewBox="0 0 24 24" fill="var(--icon-dark)"><rect x="2" y="9" width="20" height="12" rx="1.5"/><rect x="6" y="3" width="12" height="7" fill="none" stroke="var(--icon-dark)" stroke-width="2"/><rect x="5" y="13" width="8" height="2" fill="var(--gold)"/></svg></span>
        <span class="contact-text">555-384-1962</span>
      </li>
      <li class="contact-row">
        <span class="tab"></span>
        <span class="icon-box"><svg viewBox="0 0 24 24" fill="none" stroke="var(--icon-dark)" stroke-width="2"><circle cx="12" cy="12" r="9"/><ellipse cx="12" cy="12" rx="4" ry="9"/><path d="M3 12h18"/></svg></span>
        <span class="contact-text">VORASTI.COM</span>
      </li>
    </ul>
  </section>
</main>
</body>
</html>
```